Peruvian/Jewish Bat Mitzvah

We need to design the Stationary for my daughter Bat Mitzvah. Because we are originally from Peru, the decoration of the party has Peruvian textiles. We would like to honor that part of our family as well. So we would like the Stationary to reflect that. The main color should be fuchsia pink. We want the design to be joyful, colorful but elegant. I am attaching the idea that I found online and I loved and also a photo of one of the table cloth to give you an idea of the design that has to be used in the Stationary. We need 4 products:
(1) General Invitation,
(2) an Invitation to the Party,
(3) an Invitation to a Brunch at our home, and
(4) an Envelope.

Target Market(s)

American friends who don't know much about Peru and Peruvian family

Colors
e34197
b768aa
33a6d7
cadf82
e667a6
eda3c7
a54499
f59195
fece3e

Requirements
Must have
• - The design of the flowers that are in the textiles, whose picture I am attaching.
• - The combination of colors of that textiles.
• - The colors I have indicated below
• - I am attaching a number of pictures to share an idea of the design used in Peruvian textiles.
Nice to have
• We invite you to share a very special day in our lives
• as our daughter
• ROSALIND
• Is called to the Torah as a
• BAT MITZVAH
• Saturday, the Eleventh of April
• Two Thousand Twenty at 9:30 am
• Ohel Varden Congregation
• 4173 Lindcroft Avenue, NW
• Washington DC 20417
• Kiddush Luncheon following services
• Miriam and Dorian Feldkamp
• R.S.V.P. (XXX) xxx-xxxx

```html
<!DOCTYPE html>
<html lang="en">
<head>
<meta charset="utf-8">
<title>Bat Mitzvah Invitation</title>
<link href="https://fonts.googleapis.com/css2?family=Sofia&family=Dawning+of+a+New+Day&family=Dancing+Script:wght@400&display=swap" rel="stylesheet">
<style>
  :root {
    --page-bg: #f2f1ee;
    --card-bg: #ffffff;
    --title-grey: #6d6e70;
    --ink: #333333;
    --rule: #8a8a8a;
    --fuchsia: #e34197;
    --orchid: #b768aa;
    --sky: #33a6d7;
    --lime: #cadf82;
    --rose: #e667a6;
    --blush: #eda3c7;
    --plum: #a54499;
    --coral: #f59195;
    --sun: #fece3e;
  }
  html, body {
    margin: 0;
    padding: 0;
    width: 1192px;
    height: 1200px;
    overflow: hidden;
    background: var(--page-bg);
  }
  .invitation-card {
    position: absolute;
    left: 190px;
    top: 30px;
    width: 812px;
    height: 1140px;
    background: var(--card-bg);
    box-shadow: 0 1px 4px rgba(0,0,0,0.12);
    overflow: hidden;
  }
  .floral {
    position: absolute;
    left: 0;
    top: 0;
  }
  .headline {
    position: absolute;
    margin: 0;
    font-family: "Sofia", cursive;
    font-weight: 400;
    font-size: 166px;
    line-height: 1;
    color: var(--title-grey);
    white-space: nowrap;
  }
  .headline-first { left: 41px; top: 290px; }
  .headline-second { left: 185px; top: 417px; }
  .divider {
    position: absolute;
    left: 54px;
    top: 595px;
    width: 677px;
    height: 0;
    border-top: 1px solid var(--rule);
  }
  .invitation-message {
    position: absolute;
    left: 40px;
    top: 660px;
    width: 732px;
    margin: 0;
    font-family: "Dawning of a New Day", cursive;
    font-size: 30px;
    line-height: 53px;
    color: var(--ink);
    text-align: center;
  }
  .event-details {
    position: absolute;
    right: 68px;
    top: 888px;
    margin: 0;
    font-family: "Dancing Script", cursive;
    font-size: 25px;
    line-height: 29px;
    color: var(--ink);
    text-align: right;
  }
  .event-details p { margin: 0 0 29px 0; }
</style>
</head>
<body>
  <main class="invitation-card">
    <svg class="floral floral-top" width="812" height="400" viewBox="0 0 812 400" role="img" aria-label="Bright Peruvian textile-style flowers in fuchsia, orange, blue and purple on curling branches with green leaves">
      <defs>
        <linearGradient id="topBloom" x1="0" y1="1" x2="1" y2="0">
          <stop offset="0" stop-color="#f7a94a"/>
          <stop offset="0.35" stop-color="#e34197"/>
          <stop offset="0.55" stop-color="#33a6d7"/>
          <stop offset="0.75" stop-color="#b768aa"/>
          <stop offset="1" stop-color="#e667a6"/>
        </linearGradient>
      </defs>
      <path d="M60 150 C120 60 260 70 380 60 C470 40 540 10 620 5 L812 3 L812 370 C760 390 720 330 660 300 C600 280 520 290 440 270 C360 250 300 270 250 250 C180 240 100 230 60 150 Z" fill="url(#topBloom)" opacity="0.85"/>
    </svg>

    <h1 class="headline headline-first">You are</h1>
    <h1 class="headline headline-second">invited !</h1>

    <div class="divider"></div>

    <p class="invitation-message">We invite you to share a very special day in our<br>lives as our daughter ROSALIND is called to the<br>Torah as a BAT MITZVAH.</p>

    <svg class="floral floral-bottom" width="430" height="300" viewBox="0 0 430 300" style="top:845px" role="img" aria-label="Cluster of orange, pink and purple Peruvian-style flowers with green leaves in the lower corner">
      <defs>
        <linearGradient id="bottomBloom" x1="0" y1="0" x2="1" y2="1">
          <stop offset="0" stop-color="#b768aa"/>
          <stop offset="0.4" stop-color="#e34197"/>
          <stop offset="0.7" stop-color="#f7a94a"/>
          <stop offset="1" stop-color="#cadf82"/>
        </linearGradient>
      </defs>
      <path d="M0 300 L0 150 C20 60 70 20 110 30 C160 40 190 110 250 110 C310 100 360 120 400 170 C420 210 400 260 360 280 C300 300 200 295 150 300 Z" fill="url(#bottomBloom)" opacity="0.85"/>
    </svg>

    <div class="event-details">
      <p>Saturday, the Eleventh of April<br>Two Thousand Twenty at 9:30 am</p>
      <p>Ohel Varden Congregation<br>4173 Lindcroft Avenue, NW<br>Washington DC 20417</p>
    </div>
  </main>
</body>
</html>
```